New, modern business card for growing audiology practice

We need a new business card for our audiology practice. Our logo and website have recently changed (more modern) and we want our business cards to reflect this change.
We conduct hearing tests, perform earwax removals, and fit & dispense hearing aids to our patients. We are a family owned practice in which the owner is the one who works directly with the patient. I have attached logos in various formats to use, as well as two ideas I found on this website; as well as a scanned copy of our current logo. Good luck!

Industry/Entity Type

Business

Contact Information for Business Card

Company name: Maplow Hearing Center
Provider name: Peter Mulvoy, Au.D. F/ISN
Phone number: (555) 318-6042
Address: 87 W. Linden Ave. Alder Falls, OH 45871
email: maplowhearing@postvale.net
website: maplowhearing.com

Colors
000000
aaaaaa
dbdbdb
cacaca
9bcb3c
afd23c
cadf82
b1b1b1

Requirements
Must have
• My card must include information in the "details" section. In the attached images, I found a few that I liked and I would like to model after - "brisk tumblin'" and "Sound Wellness Center".
• Must be horizontal.
• Must include logos provided. I uploaded them in various file formats and various ways.
• Must match logo font, if possible, if not, please get as close as you can.
Nice to have
• I really like the idea of having a color on one side with just the logo and company name and the contact information and provider name on the other side. I also really like the idea of having the main color dominating on the logo/company side with accent of that same color on the contact side of the card.
Should not have
• Must not be vertical.

```html
<!DOCTYPE html>
<html lang="en">
<head>
<meta charset="utf-8">
<title>Maplow Hearing Center – Business Card</title>
<link href="https://fonts.googleapis.com/css2?family=Montserrat:wght@400;500;700&display=swap" rel="stylesheet">
<style>
  :root{
    --backdrop:#6e5439;
    --card-white:#ffffff;
    --card-grey:#f1f1f1;
    --ink:#1e1e1e;
    --ink-soft:#2b2b2b;
    --green:#8cbf3f;
    --green-light:#afd23c;
    --green-pale:#cadf82;
    --green-deep:#6fa33a;
    --charcoal:#2e2e2e;
  }
  *{box-sizing:border-box;margin:0;padding:0}
  html,body{width:1200px;height:1023px;overflow:hidden}
  body{background:var(--backdrop);position:relative;font-family:"Montserrat",sans-serif}

  .card{position:absolute;left:258px;width:682px;height:390px;overflow:hidden;box-shadow:0 6px 18px rgba(0,0,0,.35)}

  /* Contact side */
  .card--front{top:88px;background:radial-gradient(ellipse at 40% 50%,var(--card-white) 40%,var(--card-grey) 100%)}
  .brand-name{position:absolute;left:46px;top:40px;font-size:23px;font-weight:400;color:var(--ink);letter-spacing:.2px;white-space:nowrap}
  .provider{position:absolute;left:46px;top:128px}
  .provider__name{font-size:28px;font-weight:700;color:var(--green);line-height:1}
  .provider__title{font-size:18px;font-weight:400;color:var(--ink-soft);margin-top:4px}
  .address{position:absolute;left:46px;top:199px;font-size:19px;line-height:26px;color:var(--ink-soft);font-style:normal}
  .contacts{position:absolute;left:44px;top:275px;list-style:none}
  .contacts li{display:flex;align-items:center;height:26px;font-size:19px;color:var(--ink-soft)}
  .contacts svg{width:22px;height:20px;margin-right:17px;flex:none}
  .band{position:absolute;left:0;bottom:0;width:100%;height:16px}

  /* Brand side */
  .card--back{top:528px;background:radial-gradient(ellipse at 70% 25%,var(--green-light) 0%,var(--green) 55%,var(--green-deep) 100%)}
  .lockup{position:absolute;left:462px;top:228px;color:#fff;font-weight:400;font-size:31px;line-height:29px;letter-spacing:.3px}
  .web{position:absolute;left:373px;top:335px;color:#fff;font-size:19px;letter-spacing:.3px}
</style>
</head>
<body>

<section class="card card--front">
  <div class="brand-name">MAPLOW HEARING CENTER</div>

  <div class="provider">
    <div class="provider__name">Peter Mulvoy</div>
    <div class="provider__title">Au.D. F/ISN</div>
  </div>

  <address class="address">87 W. Linden Ave. Alder<br>Falls, OH 45871</address>

  <ul class="contacts">
    <li>
      <svg viewBox="0 0 22 20" aria-hidden="true"><path d="M5 2l3 4-2 2c1 3 4 6 7 7l2-2 4 3-2 3C10 19 3 12 2 5z" fill="var(--green)"/></svg>
      (555) 318-6042
    </li>
    <li>
      <svg viewBox="0 0 22 20" aria-hidden="true"><rect x="1" y="3" width="20" height="14" fill="var(--green)"/><path d="M1 3l10 8 10-8" fill="none" stroke="#fff" stroke-width="1.6"/></svg>
      maplowhearing@postvale.net
    </li>
    <li>
      <svg viewBox="0 0 22 20" aria-hidden="true"><circle cx="11" cy="10" r="9" fill="var(--green)"/><path d="M2 10h18M11 1v18M5 4c4 2 8 2 12 0M5 16c4-2 8-2 12 0" fill="none" stroke="#fff" stroke-width="1.2"/></svg>
      www.maplowhearing.com
    </li>
  </ul>

  <svg class="band" viewBox="0 0 682 16" preserveAspectRatio="none" aria-hidden="true">
    <polygon points="0,0 504,0 498,16 0,16" fill="var(--green)"/>
    <polygon points="514,0 682,0 682,16 508,16" fill="var(--charcoal)"/>
  </svg>
</section>

<section class="card card--back">
  <div class="lockup">MAPLOW<br>HEARING<br>CENTER</div>
  <div class="web">www.maplowhearing.com</div>
</section>

</body>
</html>
```